Marlow Crest Group (Real Estate and Investment)

A high end, clean design.
We are a real estate company with sales, asset management and investment divisions. We want to use a black and white scheme which is really high end feel. The back of the card can just be the logo (black background with the white writing) as we will probably emboss this when we print)

Target Market(s)

High level investors, high end houses for sale

Industry/Entity Type

Business

Contact Information for Business Card

Name, position, phone number and email address
Glen Varley, Managing Director, 0437259064 and glen@marlowcrest-example.com.au

Requirements
Must have
• Back of the card to be the black background with the white writing (as per the attached images). Would like the capacity to emboss the writing and logo

```html
<!DOCTYPE html>
<html lang="en">
<head>
<meta charset="utf-8">
<title>Marlow Crest Group — Business Card</title>
<link rel="stylesheet" href="https://fonts.googleapis.com/css2?family=Lato:wght@400;700&family=Montserrat:wght@600;700&display=swap">
<style>
  :root {
    --ink: #0b0b0b;
    --paper: #ffffff;
    --backdrop: #e6e6e6;
    --muted: #1c1c1c;
  }
  * { box-sizing: border-box; margin: 0; padding: 0; }
  html, body { width: 1200px; height: 680px; overflow: hidden; }
  body {
    background: var(--backdrop);
    font-family: "Lato", sans-serif;
    color: var(--ink);
  }
  .canvas {
    position: relative;
    width: 1200px;
    height: 680px;
    display: flex;
    align-items: center;
    justify-content: center;
    gap: 40px;
  }
  .card {
    position: relative;
    width: 540px;
    height: 309px;
    overflow: hidden;
    box-shadow: 0 10px 30px rgba(0,0,0,0.18);
  }

  /* Front */
  .card-front { background: var(--paper); }
  .brand {
    position: absolute;
    left: 38px;
    top: 48px;
    display: flex;
    align-items: center;
    gap: 12px;
  }
  .brand-dot {
    width: 30px;
    height: 30px;
    border: 2px solid var(--ink);
    border-radius: 50%;
  }
  .brand-name {
    font-family: "Montserrat", sans-serif;
    font-weight: 600;
    font-size: 20px;
    letter-spacing: 1.5px;
    text-transform: uppercase;
    color: var(--ink);
  }
  .person {
    position: absolute;
    left: 50px;
    top: 128px;
  }
  .person-name {
    font-family: "Montserrat", sans-serif;
    font-weight: 700;
    font-size: 22px;
    line-height: 1.1;
  }
  .person-role {
    font-size: 13px;
    margin-top: 3px;
    margin-left: 12px;
    color: var(--muted);
  }
  .contact {
    display: flex;
    align-items: center;
    gap: 10px;
    font-size: 14px;
    color: var(--muted);
  }
  .contact svg { width: 12px; height: 12px; fill: var(--ink); flex: none; }
  .contact-phone { position: absolute; left: 58px; top: 207px; }
  .contact-email { position: absolute; right: 38px; top: 220px; font-size: 13px; }
  .trim { position: absolute; left: 0; bottom: 0; width: 540px; height: 309px; }

  /* Back */
  .card-back {
    background: var(--ink);
    display: flex;
    flex-direction: column;
    align-items: center;
    justify-content: center;
    gap: 22px;
  }
  .card-back .brand-dot {
    width: 70px;
    height: 70px;
    border-color: var(--paper);
  }
  .card-back .brand-name {
    color: var(--paper);
    font-size: 26px;
    letter-spacing: 2px;
  }
</style>
</head>
<body>
<main class="canvas">
  <section class="card card-front" aria-label="Card front">
    <div class="brand">
      <span class="brand-dot"></span>
      <span class="brand-name">Marlow Crest Group</span>
    </div>

    <div class="person">
      <p class="person-name">Glen Varley</p>
      <p class="person-role">Managing Director</p>
    </div>

    <p class="contact contact-phone">
      <svg viewBox="0 0 24 24" aria-hidden="true"><path d="M6.6 10.8a15.1 15.1 0 0 0 6.6 6.6l2.2-2.2a1 1 0 0 1 1-.25 11.4 11.4 0 0 0 3.6.57 1 1 0 0 1 1 1V20a1 1 0 0 1-1 1A17 17 0 0 1 3 4a1 1 0 0 1 1-1h3.5a1 1 0 0 1 1 1c0 1.25.2 2.46.57 3.6a1 1 0 0 1-.25 1z"/></svg>
      0437 259 064
    </p>

    <p class="contact contact-email">
      <svg viewBox="0 0 24 24" aria-hidden="true"><path d="M2 5h20v14H2z M3 6l9 7 9-7" fill="none" stroke="#0b0b0b" stroke-width="2"/><path d="M2 5h20L12 12z"/></svg>
      glen@marlowcrest-example.com.au
    </p>

    <svg class="trim" viewBox="0 0 540 309" aria-hidden="true">
      <polygon points="205,252 540,252 540,264 193,264" fill="#0b0b0b"/>
      <polygon points="0,280 172,280 160,309 0,309" fill="#0b0b0b"/>
      <line x1="110" y1="280" x2="150" y2="296" stroke="#ffffff" stroke-width="2"/>
    </svg>
  </section>

  <section class="card card-back" aria-label="Card back">
    <span class="brand-dot"></span>
    <span class="brand-name">Marlow Crest Group</span>
  </section>
</main>
</body>
</html>
```